**Business Card**Designs Project** TorvaleHoldings,LLC

Im looking for a simple and elegant Business Card that has a professional Corporate look and feel. Im considering a Metal business card as well as 2 color layout, Embossed, 1 color two tone layout(File#6 like).

The card should NOT be too busy but subtle. Clean look providing Key Details.

please see uploaded files for actual logo and inspirational design i like.

See Uploaded File # 3 for Professional Logos Style

Target Market(s)

investors

Industry/Entity Type

Business

Contact Information for Business Card

Side 1 information
Torvale Holdings,LLC - Description Text below main logo = (Funding - Sales) or (Commercial - Residential) or (Property - Funding )
www.torvaleholdings.example

Side 2 Information =
Lem Korrin | Managing Broker
P 555-184-6072 | F 555-730-4158
E info@torvaleholdings.example
membership logos - see file #3 for stye and file #4 for inspiration

Side 2 = 10pt Font
BRE: 07261843
NMLS: 6827354

Colors
3277b5
5c5c5c
333333
959595
85acd3
1b1b1b
ffffff

Requirements
Must have
• Torvale Holdings, LLC **T Logo** - See Uploaded File #5 ,
• Contact Information - See Business Card Details Above
• Web address = www.torvaleholdings.example
• Membership logos - See Uploaded File #4 & 9
Nice to have
• 1 Color two tones, grey, White, Charcoal Grey, Dark Turquois, Dark blue, Slate blue,
• GOOD COMBINATIONS: White and Grey, white and Charcoal grey with a splash of blue, Charcoal grey card with White, etc..
• PLEASE TRY DARK BLUE DESIGNS
• Embossed, card designs
• Metal Business card design
Should not have
• I DONT LIKE ALOTE OF WAVE DESIGNS

```html
<!DOCTYPE html>
<html lang="en">
<head>
<meta charset="utf-8">
<title>Torvale Holdings, LLC — Business Card</title>
<link href="https://fonts.googleapis.com/css2?family=Open+Sans:wght@300;400&display=swap" rel="stylesheet">
<style>
  :root {
    --stage: #e6e6e6;
    --stage-edge: #cfcfcf;
    --charcoal: #4f4f4f;
    --charcoal-deep: #454545;
    --emboss-band: #5a5a5a;
    --emboss-ink: #434343;
    --light-band: #e2e2e2;
    --light-band-edge: #d2d2d2;
    --ink-dark: #5c5c5c;
    --ink-mid: #959595;
    --white: #ffffff;
  }
  * { box-sizing: border-box; margin: 0; padding: 0; }
  html, body { width: 1200px; height: 900px; overflow: hidden; }
  body {
    font-family: "Open Sans", Arial, sans-serif;
    font-weight: 300;
    background: radial-gradient(ellipse at 50% 40%, var(--stage) 40%, var(--stage-edge) 100%);
    position: relative;
  }
  .card {
    position: absolute;
    left: 302px;
    width: 596px;
    height: 340px;
    overflow: hidden;
    box-shadow: 0 8px 24px rgba(0,0,0,.28);
  }
  /* Front side */
  .card--front { top: 60px; background: var(--charcoal); }
  .front__band {
    position: absolute; left: 0; right: 0; top: 118px; height: 118px;
    background: var(--emboss-band);
    box-shadow: inset 0 2px 3px rgba(0,0,0,.35), inset 0 -1px 2px rgba(255,255,255,.08);
  }
  .brand { position: absolute; display: flex; align-items: center; gap: 18px; }
  .brand__mark { width: 62px; height: 62px; border-radius: 50%; }
  .brand__text { display: flex; flex-direction: column; padding-left: 18px; border-left: 1px solid currentColor; }
  .brand__name { font-size: 27px; font-weight: 400; letter-spacing: .5px; line-height: 1.1; }
  .brand__tagline { font-size: 12px; letter-spacing: 2.5px; margin-top: 6px; padding-top: 5px; border-top: 1px solid currentColor; }
  .card--front .brand { left: 60px; top: 146px; color: var(--emboss-ink); }
  .card--front .brand__mark { border: 6px solid var(--emboss-ink); }
  .front__web { position: absolute; right: 22px; bottom: 16px; font-size: 12px; color: #c8c8c8; letter-spacing: .3px; }

  /* Back side */
  .card--back { top: 470px; background: var(--charcoal); }
  .back__top { position: absolute; left: 0; right: 0; top: 0; height: 120px; background: var(--charcoal); }
  .back__middle {
    position: absolute; left: 0; right: 0; top: 120px; height: 150px;
    background: linear-gradient(180deg, var(--light-band), var(--light-band-edge));
  }
  .back__bottom { position: absolute; left: 0; right: 0; top: 270px; bottom: 0; background: var(--charcoal-deep); }
  .card--back .brand { left: 30px; top: 36px; color: var(--white); }
  .card--back .brand__mark { border: 6px solid var(--white); }
  .holder { position: absolute; right: 24px; top: 128px; text-align: right; }
  .holder__name { font-size: 30px; color: var(--ink-dark); line-height: 1.1; }
  .holder__role { font-size: 14px; color: var(--ink-dark); }
  .badges { position: absolute; right: 24px; top: 194px; display: flex; gap: 10px; }
  .badge { width: 40px; height: 40px; border: 2px solid var(--ink-mid); }
  .rule { position: absolute; left: 30px; right: 200px; top: 208px; height: 1px; background: var(--ink-mid); }
  .licenses { position: absolute; left: 30px; top: 218px; font-size: 15px; color: var(--ink-mid); letter-spacing: .3px; }
  .contacts {
    position: absolute; left: 30px; right: 24px; top: 270px; bottom: 0;
    display: flex; align-items: center; justify-content: space-between;
    color: var(--white); font-size: 16px;
  }
  .contact { display: flex; align-items: center; gap: 8px; }
  .contact svg { width: 18px; height: 18px; fill: none; stroke: var(--white); stroke-width: 1.6; }
</style>
</head>
<body>
  <section class="card card--front" aria-label="Business card front">
    <div class="front__band"></div>
    <div class="brand">
      <span class="brand__mark"></span>
      <div class="brand__text">
        <span class="brand__name">TORVALE HOLDINGS, LLC</span>
        <span class="brand__tagline">COMMERCIAL &amp; RESIDENTIAL</span>
      </div>
    </div>
    <p class="front__web">www.torvaleholdings.example</p>
  </section>

  <section class="card card--back" aria-label="Business card back">
    <div class="back__top"></div>
    <div class="back__middle"></div>
    <div class="back__bottom"></div>
    <div class="brand">
      <span class="brand__mark"></span>
      <div class="brand__text">
        <span class="brand__name">TORVALE HOLDINGS, LLC</span>
        <span class="brand__tagline">COMMERCIAL &amp; RESIDENTIAL</span>
      </div>
    </div>
    <div class="holder">
      <p class="holder__name">Lem Korrin</p>
      <p class="holder__role">Managing Broker</p>
    </div>
    <div class="badges" aria-label="Membership badges">
      <span class="badge"></span>
      <span class="badge"></span>
    </div>
    <div class="rule"></div>
    <p class="licenses">BRE: 07261843&nbsp;&nbsp;NMLS: 6827354</p>
    <div class="contacts">
      <span class="contact">
        <svg viewBox="0 0 24 24" aria-hidden="true"><path d="M5 3h4l2 5-3 2a12 12 0 0 0 6 6l2-3 5 2v4a2 2 0 0 1-2 2A17 17 0 0 1 3 5a2 2 0 0 1 2-2z"/></svg>
        555-184-6072
      </span>
      <span class="contact">
        <svg viewBox="0 0 24 24" aria-hidden="true"><rect x="3" y="9" width="18" height="10" rx="1"/><rect x="7" y="4" width="10" height="5"/><line x1="7" y1="14" x2="17" y2="14"/></svg>
        555-730-4158
      </span>
      <span class="contact">
        <svg viewBox="0 0 24 24" aria-hidden="true"><rect x="3" y="5" width="18" height="14"/><path d="M3 5l9 8 9-8"/></svg>
        info@torvaleholdings.example
      </span>
    </div>
  </section>
</body>
</html>
```